Website Design for Solar Panel Company

We are working with a company called VoltaryNX.

Some sites to use for content/competitors and inspiration:
https://www.brightmoor.example
https://prod.cld-prod.raylumen.example
https://amberfieldvolt.example
https://www.korvane.example/solarpanels

Thank you for taking the time to consider designing a website for us. We are web developers based in Stockton, CA, USA. Most of our projects go through the same process. Understanding this process may help you win a project with us. We custom-code all of our websites in-house. We don’t have any requirements as to what tools you use for your design, but we prefer Figma files. For any design that we label as four-stars, we send it to the client for review. The client picks the final design they want us to use. Once we complete this process, we will continue to show additional clients all the four-star sites and purchase them later. Your designs will have multiple chances to sell. For better chances of success, we ask that you follow these guidelines.

IMAGES:
If you use any images or icons in the design, we ask that you have a link to the asset so we can purchase the image/icon. Most of the designs we submit do not have the customer’s images on them unless they have some great images. Be creative; show us the feeling you are trying to portray with your image choices. Use any royalty-free site you choose. We subscribe to Quillex and mainly use their images, but we can purchase images outside of Quillex. PLEASE NOTE: we will not submit designs to clients with watermarks on the images.

FONTS:
We ask that you identify the fonts used in the design. This can be done in a message if you want. We typically use Marlowe Fonts and Quillex Fonts.

CONTENT:
We're always open to different content and ideas. We often submit designs with stock images so the client can see our vision. We typically take pictures after the website launch to use their images with our vision. Lorem Ipsum is fine for paragraphs, but we ask that you write the headers in correct English. We want to be able to show the vision and identify the sections of the website.

INSPIRATION:
We typically add a couple of links in the brief of websites we like to help you get started in your design.

REVISIONS:
We do not often ask for revisions of the designs unless we see something in the design that may not appeal to the client. If there are slight changes that we want to make, we do that in the development process.

FEEDBACK:
We rarely give feedback on designs during the design process. We are working on many website projects and do not have the time to provide feedback. We usually respond if your request is well thought out and asks specific questions, but a note asking “feedback, please” usually goes unanswered.

```html
<!DOCTYPE html>
<html lang="en">
<head>
<meta charset="utf-8">
<title>VoltaryNX — Home Solar, Battery &amp; EV Charging</title>
<link rel="stylesheet" href="https://fonts.googleapis.com/css2?family=Outfit:wght@300;400;500;600;700&family=Inter:wght@400;500;600&display=swap">
<style>
:root{
  --green:#8cd63f;
  --green-dark:#6cb82a;
  --ink:#111312;
  --ink-soft:#1c1f1d;
  --text:#2a2d2b;
  --muted:#6b706c;
  --line:#e3e6e2;
  --cream:#f8faef;
  --mint:#eef8e2;
  --white:#ffffff;
}
*{box-sizing:border-box;margin:0;padding:0}
html,body{width:1200px;height:4752px;overflow:hidden;background:var(--white)}
body{font-family:"Inter",Arial,sans-serif;color:var(--text);font-size:14px;line-height:1.5}
h1,h2,h3,h4,.brand,.btn{font-family:"Outfit",Arial,sans-serif}
.page{position:relative;width:1200px;height:4752px}
section,header,footer{position:relative;width:1200px;overflow:hidden}
.wrap{width:1040px;margin:0 auto;position:relative;height:100%}
.btn{display:inline-flex;align-items:center;justify-content:center;height:40px;padding:0 26px;border-radius:20px;font-size:14px;font-weight:500;text-decoration:none}
.btn-green{background:var(--green);color:var(--ink)}
.btn-dark{background:var(--ink);color:var(--white)}
.btn-outline{border:1.5px solid rgba(255,255,255,.8);color:var(--white)}
.photo{position:absolute;inset:0}

/* header */
.site-header{height:76px;background:var(--ink);color:var(--white)}
.brand{display:flex;align-items:center;gap:10px;font-size:26px;font-weight:700;letter-spacing:.5px;color:var(--white)}
.brand-dot{width:14px;height:14px;border-radius:50%;background:var(--green)}
.site-header .brand{position:absolute;left:0;top:22px}
.topline{position:absolute;right:0;top:6px;font-size:11px;color:#cfd3cf;display:flex;gap:22px}
.nav{position:absolute;right:0;top:30px;display:flex;align-items:center;gap:26px;font-size:13px}
.nav a{color:var(--white);text-decoration:none}
.nav .active{background:var(--green);color:var(--ink);padding:5px 14px;border-radius:14px}
.nav .btn{height:32px;padding:0 18px;font-size:13px}

/* hero */
.hero{height:525px}
.hero .photo{background:linear-gradient(180deg,#3c4a5c 0%,#5b6470 45%,#2b2f33 100%)}
.hero-copy{position:absolute;left:80px;top:150px;color:var(--white);width:440px}
.hero-copy h1{font-size:44px;font-weight:600;line-height:1.12;margin-bottom:30px}

/* explore */
.explore{height:380px;background:var(--cream)}
.explore h2{position:absolute;left:80px;top:58px;font-size:30px;font-weight:500;color:var(--ink)}
.explore-cards{position:absolute;left:80px;top:120px;display:flex;gap:18px}
.explore-card{width:245px;height:190px;border-radius:8px;overflow:hidden;position:relative;background:#cfd6d9}
.explore-card .label{position:absolute;left:0;right:0;bottom:0;height:40px;background:var(--white);padding:0 16px;display:flex;align-items:center;font-size:13px;font-weight:500;color:var(--ink)}
.explore-card .label.on{background:var(--green)}

/* features */
.features{height:460px;text-align:center}
.features h2{padding-top:60px;font-size:38px;font-weight:500;color:var(--ink);line-height:1.2}
.feature-row{display:flex;justify-content:center;gap:26px;margin:44px 0 40px}
.feature{width:130px;height:120px;border:1px solid var(--line);border-radius:8px;display:flex;flex-direction:column;align-items:center;justify-content:center;gap:12px;font-size:11px;color:var(--muted);line-height:1.3;padding:0 10px}

/* band */
.band{height:350px;color:var(--white);text-align:center}
.band .photo{background:linear-gradient(180deg,#1d2620,#33403a 60%,#1b211d)}
.band h2{position:relative;padding-top:52px;font-size:38px;font-weight:400}
.band-items{position:relative;display:flex;justify-content:center;gap:90px;margin:34px 0 30px}
.band-item{width:200px;font-size:12px;color:#dfe4df;display:flex;flex-direction:column;align-items:center;gap:10px}

/* about + quote */
.about{height:540px;background:var(--mint)}
.about .eyebrow{position:absolute;left:80px;top:80px;font-size:12px;color:var(--green-dark);font-weight:600}
.about h2{position:absolute;left:80px;top:104px;width:440px;font-size:42px;font-weight:500;line-height:1.15;color:var(--ink)}
.about p{position:absolute;left:80px;top:290px;width:430px;font-size:12px;color:var(--muted)}
.about .btn{position:absolute;left:80px;top:390px}
.quote-card{position:absolute;left:640px;top:70px;width:480px;height:390px;background:var(--white);border-radius:10px;padding:30px 34px;box-shadow:0 10px 30px rgba(0,0,0,.06)}
.quote-card h3{text-align:center;font-size:22px;font-weight:500;line-height:1.25;color:var(--ink);margin-bottom:24px}
.fields{display:grid;grid-template-columns:1fr 1fr;gap:14px}
.field{height:40px;border:1px solid var(--line);border-radius:6px;padding:0 12px;display:flex;align-items:center;font-size:12px;color:var(--muted)}
.field.full{grid-column:1/3}
.quote-card .btn{display:flex;width:150px;margin:24px auto 0}

/* testimonials */
.reviews{height:520px}
.reviews h2{position:absolute;left:80px;top:60px;font-size:34px;font-weight:500;color:var(--ink)}
.avatar{position:absolute;left:80px;top:150px;width:190px;height:190px;border-radius:50%;background:linear-gradient(135deg,#8fa6b8,#3e5566)}
.reviewer{position:absolute;left:80px;top:360px;font-size:14px;font-weight:600;color:var(--ink)}
.reviewer span{display:block;font-weight:400;font-size:12px;color:var(--muted)}
.review-text{position:absolute;left:340px;top:165px;width:600px;font-family:"Outfit",Arial,sans-serif;font-size:20px;line-height:1.45;color:var(--text)}
.review-text .mark{font-size:40px;color:var(--green);line-height:0;vertical-align:-12px;margin-right:6px}
.arrows{position:absolute;left:340px;top:320px;display:flex;gap:10px}
.arrow{width:34px;height:34px;border-radius:50%;border:1px solid var(--line);display:flex;align-items:center;justify-content:center}
.reviews .btn{position:absolute;left:340px;top:380px}

/* faq */
.faq{height:570px;color:var(--white)}
.faq .photo{background:linear-gradient(180deg,#1a221d,#2c3a30 55%,#161b17)}
.faq h2{position:relative;text-align:center;padding-top:54px;font-size:34px;font-weight:400}
.faq-list{position:relative;width:720px;margin:30px auto 0}
.faq-item{height:42px;border-bottom:1px solid rgba(255,255,255,.18);display:flex;justify-content:space-between;align-items:center;font-size:13px;padding:0 16px}
.faq-item.open{height:auto;background:var(--white);color:var(--text);border-radius:6px;padding:16px;display:block;border:0;margin-bottom:6px}
.faq-item.open strong{display:flex;justify-content:space-between;color:var(--green-dark);font-weight:600;margin-bottom:8px}
.faq-item.open p{font-size:12px;color:var(--muted)}
.faq .btn{position:relative;display:flex;width:130px;margin:28px auto 0}

/* articles */
.articles{height:650px;text-align:center}
.articles h2{padding-top:54px;font-size:34px;font-weight:500;color:var(--ink)}
.article-row{display:flex;justify-content:center;gap:30px;margin:36px 0 36px}
.article{width:300px;border:1px solid var(--line);border-radius:8px;overflow:hidden;text-align:center}
.article .thumb{height:170px}
.article .body{padding:16px 22px 20px}
.article .date{font-size:11px;color:var(--green-dark)}
.article h3{font-size:17px;font-weight:500;color:var(--ink);margin:6px 0 10px;line-height:1.3}
.article p{font-size:11px;color:var(--muted)}
.article .more{display:inline-block;margin-top:12px;font-size:12px;color:var(--green-dark);font-weight:500}

/* cta */
.cta{height:350px;background:var(--green)}
.cta-copy{position:absolute;left:80px;top:70px;width:420px}
.cta h2{font-size:40px;font-weight:600;line-height:1.1;color:var(--ink)}
.cta p{margin:14px 0 22px;font-size:13px;color:#243018}
.cta-photo{position:absolute;left:540px;top:0;width:660px;height:350px;background:linear-gradient(160deg,#9db7cf,#56677a 55%,#2e3a45)}

/* footer */
.site-footer{height:332px;background:var(--ink);color:#cfd3cf}
.site-footer .brand{position:absolute;left:80px;top:56px}
.foot-col{position:absolute;top:56px;font-size:12px;line-height:2}
.foot-col h4{color:var(--green);font-size:14px;font-weight:500;margin-bottom:6px}
.foot-col.contact{left:360px}
.foot-col.company{left:680px}
.foot-col .ln{display:flex;align-items:center;gap:8px}
.socials{position:absolute;left:1060px;top:56px;display:flex;flex-direction:column;gap:12px}
.socials span{width:30px;height:30px;border-radius:50%;background:var(--white)}
.copyright{position:absolute;left:0;right:0;bottom:0;height:52px;border-top:1px solid #2a2d2b;display:flex;align-items:center;justify-content:center;font-size:11px;color:#8a8f8b}
</style>
</head>
<body>
<div class="page">

<header class="site-header">
  <div class="wrap">
    <div class="brand"><span class="brand-dot"></span>VoltaryNX</div>
    <div class="topline"><span>hello@voltarynx.example</span><span>+1 (555) 014-2290</span></div>
    <nav class="nav">
      <a class="active" href="#">Home</a><a href="#">About Us</a><a href="#">Services</a><a href="#">Plans &amp; Pricing</a><a href="#">Reviews</a><a href="#">Blog</a><a href="#">Contact Us</a>
      <a class="btn btn-green" href="#">Get a Quote</a>
    </nav>
  </div>
</header>

<section class="hero">
  <div class="photo" role="img" aria-label="Modern house with solar panels on the roof at dusk"></div>
  <div class="hero-copy">
    <h1>Get record-breaking home solar &amp; save more</h1>
    <a class="btn btn-outline" href="#">Free Consultation</a>
  </div>
</section>

<section class="explore">
  <h2>Explore going solar with VoltaryNX</h2>
  <div class="explore-cards">
    <div class="explore-card"><div class="photo" role="img" aria-label="House roof with solar panels" style="background:linear-gradient(160deg,#a8c3dc,#6b7f92)"></div><div class="label on">Residential solar</div></div>
    <div class="explore-card"><div class="photo" role="img" aria-label="Home battery storage units on a wall" style="background:linear-gradient(160deg,#e6e8e6,#a9b0ad)"></div><div class="label">Energy storage</div></div>
    <div class="explore-card"><div class="photo" role="img" aria-label="Electric car charging at a home charger" style="background:linear-gradient(160deg,#d7dcdf,#8d979e)"></div><div class="label">EV charging</div></div>
    <div class="explore-card"><div class="photo" role="img" aria-label="Solar panel installation on a roof" style="background:linear-gradient(160deg,#b9c9d6,#5e7082)"></div><div class="label">Commercial solar</div></div>
  </div>
</section>

<section class="features">
  <h2>The #1 home solar, battery &amp; ev station<br>company in america</h2>
  <div class="feature-row">
    <div class="feature"><svg width="34" height="34" viewBox="0 0 34 34" fill="none" stroke="#111" stroke-width="1.6"><rect x="5" y="8" width="24" height="16" rx="1"/><path d="M5 16h24M13 8v16M21 8v16M17 24v5M11 29h12"/></svg>Quick installation</div>
    <div class="feature"><svg width="34" height="34" viewBox="0 0 34 34" fill="none" stroke="#111" stroke-width="1.6"><path d="M19 4 9 19h8l-2 11 10-15h-8z"/></svg>Efficient solar panels</div>
    <div class="feature"><svg width="34" height="34" viewBox="0 0 34 34" fill="none" stroke="#111" stroke-width="1.6"><path d="M7 19v-3a10 10 0 0 1 20 0v3"/><rect x="5" y="18" width="5" height="8" rx="2"/><rect x="24" y="18" width="5" height="8" rx="2"/></svg>24/7 customer support</div>
    <div class="feature"><svg width="34" height="34" viewBox="0 0 34 34" fill="none" stroke="#111" stroke-width="1.6"><rect x="9" y="7" width="16" height="23" rx="2"/><path d="M14 4h6M17 13l-3 6h6l-3 6"/></svg>Storage solutions</div>
    <div class="feature"><svg width="34" height="34" viewBox="0 0 34 34" fill="none" stroke="#111" stroke-width="1.6"><circle cx="17" cy="14" r="8"/><path d="M13 26h8M14 30h6"/></svg>Energy consultation</div>
  </div>
  <a class="btn btn-dark" href="#">Free Consultation</a>
</section>

<section class="band">
  <div class="photo" role="img" aria-label="Solar panels on a roof under a dark evening sky"></div>
  <h2>High tech. Hassle free.</h2>
  <div class="band-items">
    <div class="band-item"><svg width="26" height="26" viewBox="0 0 26 26" fill="none" stroke="#8cd63f" stroke-width="1.8"><circle cx="13" cy="13" r="10"/><path d="m8 13 3.5 3.5L18 10"/></svg>Best-in-class panels backed by long warranties</div>
    <div class="band-item"><svg width="26" height="26" viewBox="0 0 26 26" fill="none" stroke="#8cd63f" stroke-width="1.8"><circle cx="13" cy="13" r="10"/><path d="m8 13 3.5 3.5L18 10"/></svg>All-in-one monitoring from your phone app</div>
    <div class="band-item"><svg width="26" height="26" viewBox="0 0 26 26" fill="none" stroke="#8cd63f" stroke-width="1.8"><circle cx="13" cy="13" r="10"/><path d="m8 13 3.5 3.5L18 10"/></svg>Fast permits and install handled by our team</div>
  </div>
  <a class="btn btn-green" href="#" style="position:relative">Go solar now</a>
</section>

<section class="about">
  <div class="eyebrow">About us</div>
  <h2>Innovative energy management with VoltaryNX</h2>
  <p>It is a long established fact that a reader will be distracted by the readable content of a page when looking at its layout. The point of using Lorem Ipsum is that it has a more-or-less normal distribution of letters, as opposed to using content here, making it look like readable English.</p>
  <a class="btn btn-dark" href="#">Discover More</a>
  <form class="quote-card">
    <h3>Get a free<br>personalized quote</h3>
    <div class="fields">
      <div class="field">First name</div><div class="field">Last name</div>
      <div class="field">Email</div><div class="field">Phone</div>
      <div class="field full">Address</div>
    </div>
    <span class="btn btn-green">Get a Quote</span>
  </form>
</section>

<section class="reviews">
  <h2>What our customers say about us</h2>
  <div class="avatar" role="img" aria-label="Customer photo with home solar panels"></div>
  <div class="reviewer">Elizabeth Carter<span>Homeowner</span></div>
  <p class="review-text"><span class="mark">“</span>It is a long established fact that a reader will be distracted by the readable content of a page when looking at its layout. The point of using Lorem Ipsum is that it has a more-or-less normal distribution readable English.”</p>
  <div class="arrows">
    <span class="arrow"><svg width="12" height="12" viewBox="0 0 12 12" fill="none" stroke="#111" stroke-width="1.6"><path d="M8 2 4 6l4 4"/></svg></span>
    <span class="arrow"><svg width="12" height="12" viewBox="0 0 12 12" fill="none" stroke="#111" stroke-width="1.6"><path d="m4 2 4 4-4 4"/></svg></span>
  </div>
  <a class="btn btn-dark" href="#">View All</a>
</section>

<section class="faq">
  <div class="photo" role="img" aria-label="Residential street with solar roofs at twilight"></div>
  <h2>Frequently asked questions</h2>
  <div class="faq-list">
    <div class="faq-item"><span>How long does solar installation take?</span><span>+</span></div>
    <div class="faq-item open"><strong><span>There are many variations of passages?</span><span>−</span></strong><p>It is a long established fact that a reader will be distracted by the readable content of a page when looking at its layout. The point of using Lorem Ipsum is that it has a more-or-less normal distribution of letters.</p></div>
    <div class="faq-item"><span>How much can I save with home solar?</span><span>+</span></div>
    <div class="faq-item"><span>Do solar panels work on cloudy days?</span><span>+</span></div>
    <div class="faq-item"><span>Can I add a battery to my existing system?</span><span>+</span></div>
    <div class="faq-item"><span>What warranty comes with my panels?</span><span>+</span></div>
  </div>
  <a class="btn btn-green" href="#">View All</a>
</section>

<section class="articles">
  <h2>Articles and insights</h2>
  <div class="article-row">
    <article class="article"><div class="thumb" role="img" aria-label="Technician installing rooftop solar panels" style="background:linear-gradient(160deg,#b7cde0,#6f8496)"></div><div class="body"><div class="date">March 12, 2024</div><h3>Lorem Ipsum is simply dummy printing typesetting</h3><p>It is a long established fact that a reader will be distracted by the readable content of a page when looking at its layout.</p><span class="more">Read More →</span></div></article>
    <article class="article"><div class="thumb" role="img" aria-label="Close view of blue solar cells" style="background:linear-gradient(160deg,#4d6e9a,#1f3453)"></div><div class="body"><div class="date">March 12, 2024</div><h3>Lorem Ipsum is simply dummy printing typesetting</h3><p>It is a long established fact that a reader will be distracted by the readable content of a page when looking at its layout.</p><span class="more">Read More →</span></div></article>
    <article class="article"><div class="thumb" role="img" aria-label="Workers checking a solar array" style="background:linear-gradient(160deg,#c9d4de,#7d8a96)"></div><div class="body"><div class="date">March 12, 2024</div><h3>Lorem Ipsum is simply dummy printing typesetting</h3><p>It is a long established fact that a reader will be distracted by the readable content of a page when looking at its layout.</p><span class="more">Read More →</span></div></article>
  </div>
  <a class="btn btn-green" href="#">View All</a>
</section>

<section class="cta">
  <div class="cta-copy">
    <h2>Break the limits of traditional energy</h2>
    <p>Lorem Ipsum is simply dummy text of the printing.</p>
    <a class="btn btn-dark" href="#">Get Started</a>
  </div>
  <div class="cta-photo" role="img" aria-label="House roof covered in solar panels under blue sky"></div>
</section>

<footer class="site-footer">
  <div class="brand"><span class="brand-dot"></span>VoltaryNX</div>
  <div class="foot-col contact">
    <h4>Contact Us</h4>
    <div class="ln"><svg width="12" height="12" viewBox="0 0 12 12" fill="#8cd63f"><path d="M2.5 1h2l1 3-1.3.9a6 6 0 0 0 3 3L8 6.5l3 1v2A1.5 1.5 0 0 1 9.5 11 8.5 8.5 0 0 1 1 2.5 1.5 1.5 0 0 1 2.5 1z"/></svg>+1 (555) 014-2290</div>
    <div class="ln"><svg width="12" height="12" viewBox="0 0 12 12" fill="none" stroke="#8cd63f" stroke-width="1.3"><rect x="1" y="2.5" width="10" height="7" rx="1"/><path d="m1.5 3 4.5 3.5L10.5 3"/></svg>hello@voltarynx.example</div>
    <div class="ln"><svg width="12" height="12" viewBox="0 0 12 12" fill="#8cd63f"><path d="M6 1a3.5 3.5 0 0 0-3.5 3.5C2.5 7.5 6 11 6 11s3.5-3.5 3.5-6.5A3.5 3.5 0 0 0 6 1zm0 5a1.5 1.5 0 1 1 0-3 1.5 1.5 0 0 1 0 3z"/></svg>48 Ridgeway Lane, Fernhollow, CA</div>
  </div>
  <div class="foot-col company">
    <h4>Company</h4>
    <div>About Us</div><div>Services</div><div>Plans &amp; Pricing</div><div>Reviews</div><div>Blog</div><div>Contact Us</div>
  </div>
  <div class="socials"><span></span><span></span><span></span><span></span></div>
  <div class="copyright">© 2024 VoltaryNX. All Rights Reserved.</div>
</footer>

</div>
</body>
</html>
```